Website redesign for job agency recruitment

Please refer to the attached document, “Meridale Work Portal Outline,” for comprehensive details regarding the scope, objectives, and requirements of this website redesign project.

For imagery you can use images from this website https://www.pixaboreal.com or any other you regularly use.

Target Market(s)

Jobseekers and Companies looking for general labour

Industry/Entity Type

Services: Oil, Gas and Mining, Administrative, Construction and Trades, Warehouse and Logistics and, Manufacturing.

Number of Pages Required

5+ page

Font styles to use
Serif
Other font styles liked:
• Inter, Open-Sans or similar.

Requirements
Must have
• The requirements highlighted in the Word document attached. The final design needs to be provided in Figma including all viewports (Desktop, mobiel and tablet)
Should not have
• Website we like as a reference: www.quillvanestaffing.com, www.bexistaffing.com, www.zupran.com, www.fennickstaffing.com, www.7tpersonnel.com, www.hiringonthetrail.ca

```html
<!DOCTYPE html>
<html lang="en">
<head>
<meta charset="utf-8">
<title>Meridale Staffing — For Employers</title>
<link href="https://fonts.googleapis.com/css2?family=Inter:wght@400;500;600;700&family=Plus+Jakarta+Sans:wght@700;800&display=swap" rel="stylesheet">
<style>
:root{
  --navy:#1b2a6b;
  --navy-deep:#1a2766;
  --yellow:#fbbf24;
  --gold:#c8930b;
  --ink:#1b2a6b;
  --muted:#6b7280;
  --soft:#f6f7fb;
  --line:#e6e8f0;
  --white:#ffffff;
  --photo:#b4a489;
}
*{box-sizing:border-box;margin:0;padding:0}
html,body{width:1200px;height:2954px;overflow:hidden}
body{font-family:"Inter",sans-serif;color:var(--ink);background:var(--white);position:relative}
h1,h2,h3,.stat-value,.badge-value{font-family:"Plus Jakarta Sans",sans-serif}
.container{width:800px;margin:0 auto;position:relative}

/* nav */
.nav{height:63px;background:#e9eaf0;}
.nav .container{display:flex;align-items:center;height:63px}
.brand{display:flex;align-items:center;gap:7px;font-weight:700;font-size:13px;color:var(--navy)}
.brand-dot{width:16px;height:16px;border-radius:50%;background:var(--navy)}
.nav-links{margin-left:auto;display:flex;align-items:center;gap:22px;font-size:10px;font-weight:500;color:var(--navy)}
.btn-nav{padding:8px 13px;border-radius:5px;font-weight:600;font-size:10px}
.btn-nav.cand{background:var(--yellow);color:var(--navy)}
.btn-nav.emp{background:var(--navy);color:#fff}

/* hero */
.hero{height:405px;background:var(--navy);position:relative}
.hero .container{padding-top:77px}
.eyebrow-pill{display:inline-flex;align-items:center;gap:6px;background:rgba(255,255,255,.12);color:var(--yellow);font-size:8.5px;font-weight:700;letter-spacing:.08em;padding:4px 11px;border-radius:10px}
.hero h1{color:#fff;font-size:41px;line-height:41px;margin-top:14px;font-weight:800;letter-spacing:-.5px}
.hero h1 span{color:var(--yellow)}
.hero p{color:#b9c0dc;font-size:12px;line-height:19.5px;margin-top:20px;width:375px}
.hero-actions{display:flex;gap:11px;margin-top:26px}
.btn{display:inline-flex;align-items:center;gap:7px;height:39px;padding:0 21px;border-radius:6px;font-size:11px;font-weight:600}
.btn-primary{background:var(--yellow);color:var(--navy);box-shadow:0 4px 10px rgba(251,191,36,.35)}
.btn-ghost{border:1px solid rgba(255,255,255,.3);background:rgba(255,255,255,.08);color:#fff}

.stats{position:absolute;left:275px;top:431px;width:650px;height:75px;background:#fff;border-radius:8px;box-shadow:0 10px 25px rgba(27,42,107,.12);display:flex;z-index:2}
.stat{flex:1;display:flex;flex-direction:column;align-items:center;justify-content:center;border-right:1px solid var(--line)}
.stat:last-child{border-right:0}
.stat-value{font-size:21px;font-weight:800;color:var(--navy)}
.stat-label{font-size:7.5px;color:#9aa0b2;margin-top:3px}

/* section heads */
.section-head{text-align:center}
.eyebrow{font-size:9px;font-weight:700;letter-spacing:.12em;color:var(--gold)}
.section-head h2{font-size:25px;font-weight:800;margin-top:10px;color:var(--navy)}
.section-head p{font-size:12px;line-height:19px;color:var(--muted);margin:12px auto 0;width:430px}

/* solutions */
.solutions{height:635px;padding-top:120px}
.cards{display:flex;gap:16px;margin-top:44px}
.solution-card{width:256px;height:303px;background:var(--soft);border-radius:9px;padding:22px 22px;position:relative}
.card-num{position:absolute;right:18px;top:14px;font-family:"Plus Jakarta Sans",sans-serif;font-size:30px;font-weight:800;color:#eceef4}
.icon-box{width:32px;height:32px;border-radius:6px;background:var(--navy);display:flex;align-items:center;justify-content:center}
.solution-card h3{font-size:13.5px;font-weight:700;margin-top:22px}
.solution-card .desc{font-size:9.2px;line-height:15px;color:var(--muted);margin-top:7px}
.ticks{list-style:none;margin-top:14px}
.ticks li{display:flex;align-items:center;gap:8px;font-size:9.2px;color:#41475a;height:20px}
.btn-quote{position:absolute;left:22px;right:22px;bottom:23px;height:30px;border:1px solid #b9c0dc;border-radius:6px;background:#fff;display:flex;align-items:center;justify-content:center;font-size:9.5px;font-weight:600}
.solution-card.short .btn-quote{bottom:38px}

/* sectors */
.sectors{height:302px;background:var(--soft);padding-top:66px}
.sector-row{display:flex;gap:11px;margin-top:34px}
.sector-tile{width:151px;height:88px;background:#fff;border:1px solid var(--line);border-radius:7px;display:flex;flex-direction:column;align-items:center;justify-content:center;gap:12px;font-size:10px;font-weight:600}
.sector-icon{width:30px;height:30px;border-radius:7px;background:#eef0f7;display:flex;align-items:center;justify-content:center}

/* why */
.why{height:510px;position:relative}
.why-photo{position:absolute;left:200px;top:103px;width:378px;height:306px;border-radius:9px;background:var(--photo)}
.why-badge{position:absolute;left:461px;top:340px;width:133px;height:84px;border-radius:9px;background:var(--yellow);padding:16px 16px;box-shadow:0 8px 20px rgba(0,0,0,.15)}
.badge-value{font-size:21px;font-weight:800;color:var(--navy)}
.badge-text{font-size:9px;line-height:13px;color:var(--navy);margin-top:3px}
.why-copy{position:absolute;left:622px;top:67px;width:378px}
.why-copy h2{font-size:25px;font-weight:800;line-height:26px;margin-top:9px}
.benefits{margin-top:18px}
.benefit{display:flex;gap:12px;height:61px}
.benefit-tick{width:20px;height:20px;border-radius:5px;background:#fdf0c6;display:flex;align-items:center;justify-content:center;flex:none;margin-top:3px}
.benefit h3{font-family:"Inter",sans-serif;font-size:11px;font-weight:600}
.benefit p{font-size:9.2px;line-height:15px;color:var(--muted);margin-top:3px}

/* testimonials */
.testimonials{height:381px;background:var(--soft);padding-top:68px}
.quote-row{display:flex;gap:16px;margin-top:36px}
.quote-card{width:256px;height:165px;background:#fff;border:1px solid var(--line);border-radius:9px;padding:24px 22px}
.quote-card blockquote{font-size:9.3px;line-height:15px;color:#41475a;margin-top:14px;height:48px}
.person{display:flex;align-items:center;gap:9px;margin-top:14px}
.avatar{width:26px;height:26px;border-radius:50%;background:var(--navy);color:#fff;font-size:8px;font-weight:700;display:flex;align-items:center;justify-content:center}
.person strong{display:block;font-size:9.5px;font-weight:600}
.person span{font-size:8px;color:#9aa0b2}

/* trusted */
.trusted{height:156px;padding-top:45px;text-align:center}
.trusted-label{font-size:8px;letter-spacing:.12em;color:#c7cad4;font-weight:600}
.client-marks{display:flex;gap:15px;justify-content:center;margin-top:21px}
.client-mark{width:76px;height:36px;border-radius:6px;background:#f1f2f6}

/* cta */
.cta{height:269px;background:var(--navy);text-align:center;padding-top:64px}
.cta h2{color:#fff;font-size:25px;font-weight:800}
.cta p{color:#b9c0dc;font-size:12.5px;line-height:19.5px;width:390px;margin:12px auto 0}
.cta .btn{margin-top:26px;height:37px;padding:0 26px}

/* footer */
.footer{height:238px;background:var(--navy-deep);border-top:1px solid rgba(255,255,255,.06);position:relative}
.footer-cols{display:flex;padding-top:48px}
.footer-brand{width:206px}
.footer-brand .brand{color:#fff;font-size:11px}
.footer-brand .brand-dot{background:var(--yellow);width:12px;height:12px}
.footer-brand p{font-size:9.3px;line-height:15px;color:#8f97bd;margin-top:12px;width:190px}
.footer-col{width:207px}
.footer-col h4{font-size:9.5px;letter-spacing:.08em;color:var(--yellow);font-weight:700}
.footer-col ul{list-style:none;margin-top:12px}
.footer-col li{font-size:9.5px;color:#a8aed0;height:23px}
.footer-bottom{position:absolute;left:200px;right:200px;top:186px;border-top:1px solid rgba(255,255,255,.1);display:flex;justify-content:space-between;padding-top:20px;font-size:8px;color:#8f97bd}
.footer-bottom .legal{display:flex;gap:16px}
</style>
</head>
<body>

<header class="nav">
  <div class="container">
    <div class="brand"><span class="brand-dot"></span>Meridale Staffing</div>
    <nav class="nav-links">
      <span>Home</span><span>Sectors</span><span>Solutions</span><span>Testimonials</span>
      <span class="btn-nav cand">Candidates</span>
      <span class="btn-nav emp">Employers</span>
    </nav>
  </div>
</header>

<section class="hero">
  <div class="container">
    <span class="eyebrow-pill">
      <svg width="9" height="9" viewBox="0 0 10 10"><rect x="2" y="1" width="6" height="8" fill="none" stroke="#fbbf24" stroke-width="1.2"/><path d="M4 3h2M4 5h2M4 7h2" stroke="#fbbf24"/></svg>
      FOR EMPLOYERS
    </span>
    <h1>Hire the <span>Right People</span>,<br>Fast</h1>
    <p>From a single temp to a full project team — we deliver vetted, compliant workers across five specialist sectors, when you need them.</p>
    <div class="hero-actions">
      <span class="btn btn-primary">Request Staff
        <svg width="10" height="10" viewBox="0 0 10 10"><path d="M1 5h8M5.5 1.5L9 5 5.5 8.5" fill="none" stroke="#1b2a6b" stroke-width="1.4"/></svg></span>
      <span class="btn btn-ghost">View Solutions
        <svg width="10" height="10" viewBox="0 0 10 10"><path d="M5 1v8M1.5 5.5L5 9l3.5-3.5" fill="none" stroke="#fff" stroke-width="1.4"/></svg></span>
    </div>
  </div>
</section>

<div class="stats">
  <div class="stat"><span class="stat-value">24–48hr</span><span class="stat-label">Average Deployment</span></div>
  <div class="stat"><span class="stat-value">850+</span><span class="stat-label">Active Clients</span></div>
  <div class="stat"><span class="stat-value">98%</span><span class="stat-label">Fill Rate</span></div>
  <div class="stat"><span class="stat-value">22%</span><span class="stat-label">Avg Cost Savings</span></div>
</div>

<section class="solutions">
  <div class="container">
    <div class="section-head">
      <div class="eyebrow">OUR SOLUTIONS</div>
      <h2>Staffing That Scales with You</h2>
      <p>Choose the model that fits your business. All solutions come with dedicated account management and full compliance.</p>
    </div>
    <div class="cards">
      <article class="solution-card">
        <span class="card-num">01</span>
        <div class="icon-box"><svg width="14" height="14" viewBox="0 0 14 14"><circle cx="7" cy="7" r="5.5" fill="none" stroke="#fbbf24" stroke-width="1.3"/><path d="M7 4v3l2 1.3" fill="none" stroke="#fbbf24" stroke-width="1.3"/></svg></div>
        <h3>Temporary &amp; Contract</h3>
        <p class="desc">Flexible, on-demand workers to cover peaks, projects and short-term gaps. Deployed within 24–48 hours.</p>
        <ul class="ticks">
          <li><svg width="9" height="9" viewBox="0 0 10 10"><path d="M1 5.5l2.5 2.5L9 2" fill="none" stroke="#fbbf24" stroke-width="1.6"/></svg>24-hour candidate deployment</li>
          <li><svg width="9" height="9" viewBox="0 0 10 10"><path d="M1 5.5l2.5 2.5L9 2" fill="none" stroke="#fbbf24" stroke-width="1.6"/></svg>Fully vetted and compliant workers</li>
          <li><svg width="9" height="9" viewBox="0 0 10 10"><path d="M1 5.5l2.5 2.5L9 2" fill="none" stroke="#fbbf24" stroke-width="1.6"/></svg>Payroll and HR administration included</li>
          <li><svg width="9" height="9" viewBox="0 0 10 10"><path d="M1 5.5l2.5 2.5L9 2" fill="none" stroke="#fbbf24" stroke-width="1.6"/></svg>Flexible shift patterns and volume hire</li>
        </ul>
        <span class="btn-quote">Get a Quote</span>
      </article>
      <article class="solution-card short">
        <span class="card-num">02</span>
        <div class="icon-box"><svg width="14" height="14" viewBox="0 0 14 14"><circle cx="5" cy="5" r="2.2" fill="none" stroke="#fbbf24" stroke-width="1.2"/><path d="M1 12c0-2.5 2-4 4-4s4 1.5 4 4" fill="none" stroke="#fbbf24" stroke-width="1.2"/><circle cx="10" cy="5" r="1.8" fill="none" stroke="#fbbf24" stroke-width="1.2"/><path d="M10.5 8.2c1.5.3 2.5 1.6 2.5 3.6" fill="none" stroke="#fbbf24" stroke-width="1.2"/></svg></div>
        <h3>Permanent Recruitment</h3>
        <p class="desc">End-to-end hiring for long-term roles — from job brief through to placement and aftercare.</p>
        <ul class="ticks">
          <li><svg width="9" height="9" viewBox="0 0 10 10"><path d="M1 5.5l2.5 2.5L9 2" fill="none" stroke="#fbbf24" stroke-width="1.6"/></svg>Dedicated sector-specialist consultants</li>
          <li><svg width="9" height="9" viewBox="0 0 10 10"><path d="M1 5.5l2.5 2.5L9 2" fill="none" stroke="#fbbf24" stroke-width="1.6"/></svg>Rigorous screening and reference checks</li>
          <li><svg width="9" height="9" viewBox="0 0 10 10"><path d="M1 5.5l2.5 2.5L9 2" fill="none" stroke="#fbbf24" stroke-width="1.6"/></svg>Guarantee period on all placements</li>
          <li><svg width="9" height="9" viewBox="0 0 10 10"><path d="M1 5.5l2.5 2.5L9 2" fill="none" stroke="#fbbf24" stroke-width="1.6"/></svg>Employer branding and advert optimisation</li>
        </ul>
        <span class="btn-quote">Get a Quote</span>
      </article>
      <article class="solution-card">
        <span class="card-num">03</span>
        <div class="icon-box"><svg width="14" height="14" viewBox="0 0 14 14"><path d="M2 4h10M2 7h10M2 10h10" stroke="#fbbf24" stroke-width="1.2"/><circle cx="5" cy="4" r="1.2" fill="#1b2a6b" stroke="#fbbf24"/><circle cx="9" cy="7" r="1.2" fill="#1b2a6b" stroke="#fbbf24"/><circle cx="6" cy="10" r="1.2" fill="#1b2a6b" stroke="#fbbf24"/></svg></div>
        <h3>Managed Services</h3>
        <p class="desc">Outsource your workforce management to us — on-site teams, vendor management and full compliance.</p>
        <ul class="ticks">
          <li><svg width="9" height="9" viewBox="0 0 10 10"><path d="M1 5.5l2.5 2.5L9 2" fill="none" stroke="#fbbf24" stroke-width="1.6"/></svg>On-site managed service programmes</li>
          <li><svg width="9" height="9" viewBox="0 0 10 10"><path d="M1 5.5l2.5 2.5L9 2" fill="none" stroke="#fbbf24" stroke-width="1.6"/></svg>Recruitment process outsourcing (RPO)</li>
          <li><svg width="9" height="9" viewBox="0 0 10 10"><path d="M1 5.5l2.5 2.5L9 2" fill="none" stroke="#fbbf24" stroke-width="1.6"/></svg>Consolidated billing and reporting</li>
          <li><svg width="9" height="9" viewBox="0 0 10 10"><path d="M1 5.5l2.5 2.5L9 2" fill="none" stroke="#fbbf24" stroke-width="1.6"/></svg>Workforce analytics and cost reduction</li>
        </ul>
        <span class="btn-quote">Get a Quote</span>
      </article>
    </div>
  </div>
</section>

<section class="sectors">
  <div class="container">
    <div class="section-head">
      <div class="eyebrow">SECTOR EXPERTISE</div>
      <h2>We Recruit Across</h2>
    </div>
    <div class="sector-row">
      <div class="sector-tile"><span class="sector-icon"><svg width="14" height="14" viewBox="0 0 14 14"><rect x="1.5" y="4" width="11" height="8" rx="1.5" fill="none" stroke="#6b78b0" stroke-width="1.1"/><path d="M5 4V2.5h4V4M1.5 7.5h11" fill="none" stroke="#6b78b0" stroke-width="1.1"/></svg></span>Oil, Gas &amp; Mining</div>
      <div class="sector-tile"><span class="sector-icon"><svg width="14" height="14" viewBox="0 0 14 14"><rect x="1.5" y="4" width="11" height="8" rx="1.5" fill="none" stroke="#6b78b0" stroke-width="1.1"/><path d="M5 4V2.5h4V4M1.5 7.5h11" fill="none" stroke="#6b78b0" stroke-width="1.1"/></svg></span>Administrative</div>
      <div class="sector-tile"><span class="sector-icon"><svg width="14" height="14" viewBox="0 0 14 14"><rect x="1.5" y="4" width="11" height="8" rx="1.5" fill="none" stroke="#6b78b0" stroke-width="1.1"/><path d="M5 4V2.5h4V4M1.5 7.5h11" fill="none" stroke="#6b78b0" stroke-width="1.1"/></svg></span>Construction &amp; Trades</div>
      <div class="sector-tile"><span class="sector-icon"><svg width="14" height="14" viewBox="0 0 14 14"><rect x="1.5" y="4" width="11" height="8" rx="1.5" fill="none" stroke="#6b78b0" stroke-width="1.1"/><path d="M5 4V2.5h4V4M1.5 7.5h11" fill="none" stroke="#6b78b0" stroke-width="1.1"/></svg></span>Warehouse &amp; Logistics</div>
      <div class="sector-tile"><span class="sector-icon"><svg width="14" height="14" viewBox="0 0 14 14"><rect x="1.5" y="4" width="11" height="8" rx="1.5" fill="none" stroke="#6b78b0" stroke-width="1.1"/><path d="M5 4V2.5h4V4M1.5 7.5h11" fill="none" stroke="#6b78b0" stroke-width="1.1"/></svg></span>Manufacturing</div>
    </div>
  </div>
</section>

<section class="why">
  <div class="why-photo" role="img" aria-label="Photo of a drilling rig at a remote desert work site"></div>
  <div class="why-badge">
    <div class="badge-value">98%</div>
    <div class="badge-text">Fill rate across all sectors</div>
  </div>
  <div class="why-copy">
    <div class="eyebrow">WHY PARTNER WITH US</div>
    <h2>A Recruitment Partner That Delivers</h2>
    <div class="benefits">
      <div class="benefit"><span class="benefit-tick"><svg width="9" height="9" viewBox="0 0 10 10"><path d="M1 5.5l2.5 2.5L9 2" fill="none" stroke="#e0a50f" stroke-width="1.6"/></svg></span><div><h3>Speed</h3><p>Candidates deployed within 24–48 hours. We hold a bench of pre-screened, available workers ready to go.</p></div></div>
      <div class="benefit"><span class="benefit-tick"><svg width="9" height="9" viewBox="0 0 10 10"><path d="M1 5.5l2.5 2.5L9 2" fill="none" stroke="#e0a50f" stroke-width="1.6"/></svg></span><div><h3>Compliance</h3><p>Every worker is right-to-work checked, reference-verified and holds all required certifications for their sector.</p></div></div>
      <div class="benefit"><span class="benefit-tick"><svg width="9" height="9" viewBox="0 0 10 10"><path d="M1 5.5l2.5 2.5L9 2" fill="none" stroke="#e0a50f" stroke-width="1.6"/></svg></span><div><h3>Dedicated Account Managers</h3><p>A named contact who understands your business, your site and your workforce needs.</p></div></div>
      <div class="benefit"><span class="benefit-tick"><svg width="9" height="9" viewBox="0 0 10 10"><path d="M1 5.5l2.5 2.5L9 2" fill="none" stroke="#e0a50f" stroke-width="1.6"/></svg></span><div><h3>Cost Transparency</h3><p>Clear, competitive rates with no hidden fees. Consolidated invoicing and full reporting.</p></div></div>
      <div class="benefit"><span class="benefit-tick"><svg width="9" height="9" viewBox="0 0 10 10"><path d="M1 5.5l2.5 2.5L9 2" fill="none" stroke="#e0a50f" stroke-width="1.6"/></svg></span><div><h3>National Reach</h3><p>One agency, nationwide coverage. We recruit and deploy across the UK from multiple regional hubs.</p></div></div>
    </div>
  </div>
</section>

<section class="testimonials">
  <div class="container">
    <div class="section-head">
      <div class="eyebrow">CLIENT FEEDBACK</div>
      <h2>What Our Clients Say</h2>
    </div>
    <div class="quote-row">
      <article class="quote-card">
        <svg width="18" height="10" viewBox="0 0 18 10"><circle cx="5" cy="5" r="4" fill="#fbbf24" opacity=".7"/><circle cx="13" cy="5" r="4" fill="#fbbf24" opacity=".7"/></svg>
        <blockquote>"Meridale Staffing has been our go-to staffing partner for 5 years. Their speed and quality of candidates is unmatched."</blockquote>
        <div class="person"><span class="avatar">RH</span><div><strong>Rowena Hale</strong><span>HR Director, Brickline Group</span></div></div>
      </article>
      <article class="quote-card">
        <svg width="18" height="10" viewBox="0 0 18 10"><circle cx="5" cy="5" r="4" fill="#fbbf24" opacity=".7"/><circle cx="13" cy="5" r="4" fill="#fbbf24" opacity=".7"/></svg>
        <blockquote>"They mobilised 40 warehouse operatives in under a week for our peak season. Absolutely reliable."</blockquote>
        <div class="person"><span class="avatar">DC</span><div><strong>Dorian Cole</strong><span>Operations Manager, Northvale Freight</span></div></div>
      </article>
      <article class="quote-card">
        <svg width="18" height="10" viewBox="0 0 18 10"><circle cx="5" cy="5" r="4" fill="#fbbf24" opacity=".7"/><circle cx="13" cy="5" r="4" fill="#fbbf24" opacity=".7"/></svg>
        <blockquote>"The managed service programme they run on our site has reduced our agency spend by 22% year-on-year."</blockquote>
        <div class="person"><span class="avatar">SO</span><div><strong>Selin Okafor</strong><span>Procurement Lead, Crestore Mining</span></div></div>
      </article>
    </div>
  </div>
</section>

<section class="trusted">
  <div class="trusted-label">TRUSTED BY LEADING COMPANIES</div>
  <div class="client-marks">
    <span class="client-mark"></span><span class="client-mark"></span><span class="client-mark"></span>
    <span class="client-mark"></span><span class="client-mark"></span><span class="client-mark"></span>
  </div>
</section>

<section class="cta">
  <h2>Ready to Build Your Workforce?</h2>
  <p>Tell us what you need. A dedicated consultant will respond within 2 hours during business days.</p>
  <span class="btn btn-primary">Request Staff Now
    <svg width="10" height="10" viewBox="0 0 10 10"><path d="M1 5h8M5.5 1.5L9 5 5.5 8.5" fill="none" stroke="#1b2a6b" stroke-width="1.4"/></svg></span>
</section>

<footer class="footer">
  <div class="container footer-cols">
    <div class="footer-brand">
      <div class="brand"><span class="brand-dot"></span>Meridale Staffing</div>
      <p>Your trusted national recruitment partner connecting talent with opportunity.</p>
    </div>
    <div class="footer-col"><h4>QUICK LINKS</h4><ul><li>Home</li><li>Sectors</li><li>About Us</li><li>Contact</li></ul></div>
    <div class="footer-col"><h4>CANDIDATES</h4><ul><li>Browse Jobs</li><li>Submit CV</li></ul></div>
    <div class="footer-col"><h4>EMPLOYERS</h4><ul><li>Solutions</li><li>Request Staff</li></ul></div>
  </div>
  <div class="footer-bottom">
    <span>© 2026 Meridale Staffing. All rights reserved.</span>
    <span class="legal"><span>Privacy Policy</span><span>Terms of Service</span></span>
  </div>
</footer>

</body>
</html>
```